Tranvik Leasing Corp - Business Card Design

Need a new modern designed business card that is different and stands out to represent my equipment financing company. Tranvik Leasing Corp finances all types of equipment and all types of industries. We like to do equipment financing a different way by putting customers first and want our card to represent that different approach to business. I want a card that some remembers when they receive it so it sticks in their mind and makes that wow impression.

Card should have a black background so the logo stands out. It can be horizontial or vertical or a combination of both.

Front of card information is below that shows the information that would go on my card. That is where I want a different look or design to stand out. The front could be split black/orange colour so the logo could pop on black side and information on orange side with different lettering. Just outside the box thinking on the front of the card. Open to any type of design.

Back of card is below which i I like unless you have a different spin to provide or a different idea that would make the card better as I am open to anything that looks great.

Target Market(s)

Tranvik Leasing Corp deals with business owners in all industries.

Industry/Entity Type

Business

Contact Information for Business Card

Colors

Designer to choose colors to be used in the design.

Requirements
Must have
• Modern
• Different
• Stand Out
• Makes an Impression

```html
<!DOCTYPE html>
<html lang="en">
<head>
<meta charset="utf-8">
<title>Tranvik Leasing Corp – Business Card</title>
<link rel="stylesheet" href="https://fonts.googleapis.com/css2?family=Anton&family=Montserrat:wght@700;800&family=Open+Sans:wght@400;600&display=swap">
<style>
  :root {
    --stage: #2b2b2b;
    --black: #050505;
    --black-soft: #1c1c1c;
    --orange: #f08a2a;
    --orange-deep: #e46f1a;
    --band: #3a3a3a;
    --ink: #0a0a0a;
    --white: #ffffff;
    --icon-red: #e8443a;
    --brand-orange: #f5a032;
  }
  * { box-sizing: border-box; margin: 0; padding: 0; }
  html, body {
    width: 1200px; height: 1015px; overflow: hidden;
    background: var(--stage);
  }
  .canvas { position: relative; width: 1200px; height: 1015px; }

  .card {
    position: absolute; top: 215px;
    width: 340px; height: 585px;
    border-radius: 22px; overflow: hidden;
  }

  /* Back: logo side */
  .card-back {
    left: 215px;
    background: radial-gradient(ellipse at 60% 35%, var(--black-soft), var(--black) 70%);
    display: flex; flex-direction: column; align-items: center; justify-content: center;
    gap: 22px;
  }
  .brand-mark {
    font-family: "Montserrat", sans-serif; font-weight: 800;
    font-size: 30px; line-height: 1.1; text-align: center;
    color: var(--brand-orange);
  }
  .tagline {
    font-family: "Montserrat", sans-serif; font-weight: 700;
    font-size: 15px; letter-spacing: 0.5px; color: var(--white);
  }

  /* Front: contact side */
  .card-front {
    left: 645px;
    background: linear-gradient(160deg, var(--orange) 0%, var(--orange-deep) 100%);
  }
  .side-band {
    position: absolute; left: 40px; top: 0; bottom: 0; width: 26px;
    background: var(--band);
  }
  .front-brand {
    position: absolute; top: 34px; right: 24px;
    font-family: "Montserrat", sans-serif; font-weight: 800;
    font-size: 14px; color: var(--ink); text-align: right; line-height: 1.15;
  }
  .person { position: absolute; top: 120px; left: 92px; }
  .person-name {
    font-family: "Anton", sans-serif; font-size: 40px; line-height: 1;
    color: var(--ink); letter-spacing: 0.5px;
  }
  .person-role {
    font-family: "Open Sans", sans-serif; font-size: 14px; color: var(--ink);
    margin-top: 4px;
  }

  .contact-list { position: absolute; top: 250px; left: 0; right: 0; list-style: none; }
  .contact-item { position: relative; height: 82px; }
  .contact-icon {
    position: absolute; left: 31px; top: 0;
    width: 44px; height: 44px; background: var(--black);
    display: flex; align-items: center; justify-content: center;
  }
  .contact-icon svg { width: 22px; height: 22px; }
  .contact-text {
    position: absolute; left: 92px; top: 10px;
    font-family: "Open Sans", sans-serif; font-size: 16px; color: var(--white);
  }
  .contact-rule {
    position: absolute; left: 92px; top: 46px;
    width: 90px; height: 2px; background: var(--ink);
  }

  .social-row {
    position: absolute; left: 31px; bottom: 44px;
    display: flex; align-items: center; gap: 12px;
  }
  .social-dot { width: 18px; height: 18px; background: var(--ink); }
  .social-handle {
    margin-left: 14px;
    font-family: "Open Sans", sans-serif; font-size: 16px; color: var(--white);
  }
</style>
</head>
<body>
<main class="canvas">

  <section class="card card-back" aria-label="Card back">
    <div class="brand-mark">Tranvik<br>Leasing Corp</div>
    <p class="tagline">EQUIPMENT FINANCING EXPERTS</p>
  </section>

  <section class="card card-front" aria-label="Card front">
    <div class="side-band"></div>
    <div class="front-brand">Tranvik<br>Leasing Corp</div>

    <div class="person">
      <h1 class="person-name">OWEN HARTLEY</h1>
      <p class="person-role">President</p>
    </div>

    <ul class="contact-list">
      <li class="contact-item">
        <span class="contact-icon">
          <svg viewBox="0 0 24 24" aria-hidden="true"><path fill="var(--icon-red)" d="M6.6 10.8a15.1 15.1 0 0 0 6.6 6.6l2.2-2.2a1 1 0 0 1 1-.25 11.4 11.4 0 0 0 3.6.57 1 1 0 0 1 1 1V20a1 1 0 0 1-1 1A17 17 0 0 1 3 4a1 1 0 0 1 1-1h3.5a1 1 0 0 1 1 1c0 1.25.2 2.45.57 3.57a1 1 0 0 1-.25 1z"/></svg>
        </span>
        <span class="contact-text">555.010.4821</span>
        <span class="contact-rule"></span>
      </li>
      <li class="contact-item">
        <span class="contact-icon">
          <svg viewBox="0 0 24 24" aria-hidden="true"><rect x="2" y="5" width="20" height="14" fill="var(--icon-red)"/><path d="M2 5l10 8 10-8" fill="none" stroke="var(--black)" stroke-width="1.6"/></svg>
        </span>
        <span class="contact-text">owen@tranvikleasing.ca</span>
        <span class="contact-rule"></span>
      </li>
      <li class="contact-item">
        <span class="contact-icon">
          <svg viewBox="0 0 24 24" aria-hidden="true" fill="none" stroke="var(--icon-red)" stroke-width="1.6"><circle cx="12" cy="12" r="9"/><ellipse cx="12" cy="12" rx="4" ry="9"/><path d="M3 12h18M5 7h14M5 17h14"/></svg>
        </span>
        <span class="contact-text">www.tranvikleasing.ca</span>
        <span class="contact-rule"></span>
      </li>
    </ul>

    <div class="social-row">
      <span class="social-dot"></span>
      <span class="social-dot"></span>
      <span class="social-dot"></span>
      <span class="social-handle">@Tranvikleasing</span>
    </div>
  </section>

</main>
</body>
</html>
```